International travel site frontpage redesign

We sell tours to Scandinavia through our website www.velmora-journeys.com. The website has become a bit old fashioned and we are in the process of making the website responsive. As you can see from the attached pictures the website will be wider with the responsive design, and our current design does not fit anymore.

Here is what we are looking for:
- A website that reflects a trustworthy and quality oriented company.
- Making the website more modern looking, but still recognisable (we want to keep the colours).
- keeping in mind that the age group of our customers are from 20-80 years old (most in their 60s).
- We want to remove the popular tours part and are instead looking to replace this with picture boxes the following subjects Scandinavia Specialist, Special Offers, Contact, Norway (or Norway Tours), Sweden (or Sweden Tours), Iceland (or Iceland Tours), Combination Tours. Possibly also Lapland, Winter, Northern Lights, Fjords and Capitals. Some of these categories can be smaller or perhaps half boxes; i.e. Winter and Northern lights in one. If we end up with four boxes per line perhaps we could add a social media box next to the three first ones.
- The above means that the left hand meny with Norway Tours, Sweden Tours etc will be redundant.
- we will add another line to the search Box (on the top): Destinations
- The top menu will have the same categories, but we need to add languages as the website will be in English and German.
- The footer must be changed
- We can take away the box to the right where it says "your window to booking the best of our world"

Reason: One of the decission makers had to go away on business last minute.

Target Market(s)

Travelling to Scandinavia is not low cost, so the website needs to appeal to those that can afford to travel to our destination.
The age group of our customers are from 20-80 years old (most in their 60s).

Industry/Entity Type

Travel

Number of Pages Required

1 page

Requirements
Should not have
• Flashy or cheap looking special offers...

```html
<!DOCTYPE html>
<html lang="en">
<head>
<meta charset="utf-8">
<title>Velmora Journeys – Tours to Scandinavia</title>
<link rel="stylesheet" href="https://fonts.googleapis.com/css2?family=Open+Sans:wght@300;400;600;700&family=Crimson+Text:wght@400;600&display=swap">
<style>
:root{
  --red:#a8121a;
  --red-dark:#8a0d13;
  --ink:#333333;
  --muted:#777777;
  --line:#dddddd;
  --paper:#ffffff;
  --mist:#f5f5f5;
  --band-gray:#ebebeb;
  --sky:#3a86d4;
  --footer:#2f2f2f;
  --footer-deep:#1e1e1e;
  --star:#f6c12a;
}
*{margin:0;padding:0;box-sizing:border-box}
html,body{width:1200px;height:3103px;overflow:hidden}
body{position:relative;background:var(--paper);font-family:"Open Sans",Arial,sans-serif;color:var(--ink)}
.abs{position:absolute}

/* header */
.site-header{left:0;top:0;width:1200px;height:114px;background:var(--paper);box-shadow:0 2px 4px rgba(0,0,0,.08);z-index:2}
.brand{left:110px;top:36px;display:flex;align-items:center;gap:12px;font-family:"Crimson Text",Georgia,serif;font-size:30px;letter-spacing:1px;color:#222}
.brand-mark{width:16px;height:16px;background:var(--red)}
.contact-row{right:110px;top:22px;display:flex;align-items:center;gap:10px}
.phone{display:flex;align-items:center;gap:8px;color:var(--red);font-size:16px;margin-right:8px}
.social-dot{width:28px;height:28px;border:1.5px solid #777;border-radius:50%}
.main-nav{right:110px;top:74px;display:flex;gap:22px;font-size:13px;font-weight:600;color:#333}
.main-nav .active{color:var(--red)}

/* hero */
.hero{left:0;top:114px;width:1200px;height:511px;background:linear-gradient(180deg,#c9cdd2 0%,#e4e6e9 45%,#f3f4f5 75%,#dfe3e6 100%)}
.hero-arrow{top:238px;width:42px;height:42px;border-radius:50%;background:rgba(90,90,90,.55)}
.search-box{left:110px;top:172px;width:358px;height:366px;background:rgba(45,45,45,.88);border-radius:3px;padding:22px 24px;color:#fff}
.search-box h2{font-family:"Crimson Text",Georgia,serif;font-weight:400;font-size:28px;line-height:1}
.search-box .intro{font-size:15px;color:#aaa;margin-top:14px;line-height:1.4}
.field-grid{display:grid;grid-template-columns:1fr 1fr;gap:12px 22px;margin-top:16px}
.field-grid label{display:block;font-size:15px;margin-bottom:6px}
.field{height:30px;background:#fff;border:1px solid #999;position:relative}
.field.select::after{content:"";position:absolute;right:0;top:0;width:22px;height:28px;border-left:1px solid #bbb;background:#eee}
.field.select::before{content:"";position:absolute;right:7px;top:12px;border:4px solid transparent;border-top-color:#666;z-index:1}
.btn-red{display:block;background:linear-gradient(#c31f25,var(--red-dark));color:#fff;text-align:center;font-weight:600}
.search-btn{margin:24px auto 0;width:286px;height:50px;line-height:50px;font-size:21px}

/* sections */
.section-title{width:1200px;left:0;text-align:center;font-weight:300;font-size:33px;color:#444}
.section-lede{width:1200px;left:0;text-align:center;font-size:12px;line-height:1.75;color:#888}
.discover{left:0;top:625px;width:1200px;height:610px;background:var(--mist)}
.gallery{left:108px;top:770px;width:978px;height:347px;background:#fff;padding:14px}
.shot{position:absolute;border-radius:5px}
.find-btn{left:476px;top:1150px;width:246px;height:50px;line-height:50px;font-size:21px}

/* tours */
.tour-card{width:233px;height:396px;border:1px solid var(--line);background:#fff;border-radius:4px;overflow:hidden}
.tour-photo{height:195px}
.tour-card h3{text-align:center;font-size:17px;font-weight:700;margin-top:14px;color:#333}
.tour-sub{text-align:center;font-size:13.5px;line-height:1.4;color:#444;margin:4px 18px 0}
.tour-card hr{border:0;border-top:1px solid var(--line);margin:12px 12px 10px}
.tour-desc{text-align:center;font-size:12.5px;line-height:1.45;color:#444;margin:0 14px}
.price-band{position:absolute;left:0;bottom:0;width:100%;height:45px;background:var(--red);color:#fff;display:flex;justify-content:space-between;align-items:center;padding:0 12px;font-size:16px}
.stars{color:var(--star);font-size:15px;letter-spacing:1px}

/* testimonials */
.testimonials{left:0;top:2303px;width:1200px;height:318px;background:var(--band-gray)}
.testimonials h2{left:114px;top:88px;font-size:29px;font-weight:700;color:#333;letter-spacing:.3px}
.testimonials .summary{left:114px;top:146px;width:480px;font-size:13px;line-height:1.7;color:#444}
.quote-box{left:658px;top:83px;width:428px;height:120px;background:#fff;border-radius:4px;padding:18px 22px;font-size:13px;line-height:1.7;color:#444}
.quote-box::after{content:"";position:absolute;left:48px;bottom:-12px;border:12px solid transparent;border-bottom:0;border-top-color:#fff}
.chev{font-size:26px;color:#999;font-weight:300}
.author{left:690px;top:218px;display:flex;align-items:center;gap:16px;font-size:13px;color:#333}
.avatar{width:50px;height:50px;border-radius:50%;background:linear-gradient(#8a8f96,#4a4e54)}

/* tweet band */
.tweet-band{left:0;top:2621px;width:1200px;height:94px;background:var(--sky);color:#fff}
.tweet-dot{left:126px;top:32px;width:30px;height:30px;border-radius:50%;background:#fff}
.tweet-text{left:207px;top:36px;font-size:14px}
.tweet-nav{top:32px;width:30px;height:30px;background:#fff;color:var(--sky);text-align:center;line-height:28px;font-size:20px}

/* footer */
.site-footer{left:0;top:2715px;width:1200px;height:331px;background:var(--footer);color:#9a9a9a}
.site-footer h4{position:absolute;top:56px;font-size:19px;font-weight:600;color:#fff;letter-spacing:.2px}
.about-text{left:114px;top:104px;width:320px;font-size:12.5px;line-height:1.75}
.quick-links{left:490px;top:98px;width:146px;list-style:none;font-size:12.5px}
.quick-links li{height:28px;line-height:28px;border-bottom:1px solid #474747}
.news-text{left:720px;top:104px;width:330px;font-size:12.5px;line-height:1.75}
.email{left:720px;top:163px;width:252px;height:44px;background:#fff;color:#999;font-size:13px;padding:13px 12px}
.subscribe{left:972px;top:163px;width:120px;height:44px;line-height:44px;font-size:14px;background:var(--red)}
.foot-social{top:232px;width:22px;height:22px;border:1.5px solid #aaa;border-radius:50%}
.bottom-bar{left:0;top:3046px;width:1200px;height:57px;background:var(--footer-deep);color:#ccc;font-size:13px}
.pay-card{top:14px;width:46px;height:28px;background:#f4f4f4;border-radius:3px}
</style>
</head>
<body>

<header class="site-header abs">
  <div class="brand abs"><span class="brand-mark"></span>VELMORA JOURNEYS</div>
  <div class="contact-row abs">
    <span class="phone">
      <svg width="26" height="26" viewBox="0 0 26 26"><circle cx="13" cy="13" r="12" fill="none" stroke="#777" stroke-width="1.5"/><path d="M8 9c0-1 1-2 2-2h6c1 0 2 1 2 2v1h-3V9h-4v1H8zM9 12h8l1 6H8z" fill="#777"/></svg>
      0100-555-01234
    </span>
    <span class="social-dot"></span><span class="social-dot"></span><span class="social-dot"></span><span class="social-dot"></span>
  </div>
  <nav class="main-nav abs">
    <span class="active">HOME</span><span>FJORDS</span><span>CAPITALS</span><span>CRUISES</span><span>WINTER</span><span>GALLERY</span><span>CONTACT US</span>
  </nav>
</header>

<section class="hero abs" role="img" aria-label="Snowy mountain forest with a smiling skiing couple holding skis">
  <span class="hero-arrow abs" style="left:27px"><svg width="42" height="42"><path d="M24 13l-8 8 8 8" fill="none" stroke="#fff" stroke-width="3"/></svg></span>
  <span class="hero-arrow abs" style="right:27px"><svg width="42" height="42"><path d="M18 13l8 8-8 8" fill="none" stroke="#fff" stroke-width="3"/></svg></span>
</section>

<form class="search-box abs">
  <h2>Scandinavia Search</h2>
  <p class="intro">Lorem ipsum dolor sit amet consectetur adipiscing elit...</p>
  <div class="field-grid">
    <div><label>Tour Type:</label><div class="field select"></div></div>
    <div><label>Tour Selection:</label><div class="field select"></div></div>
    <div><label>Travel Periods:</label><div class="field select"></div></div>
    <div><label>Free Search:</label><div class="field"></div></div>
  </div>
  <span class="btn-red search-btn">Start Your Search</span>
</form>

<section class="discover abs">
  <h2 class="section-title abs" style="top:30px">Discover Scandinavia</h2>
  <p class="section-lede abs" style="top:88px">Lorem ipsum dolor sit amet, consectetur adipiscing elit. Etiam faucibus<br>diam a nibh ornare dignissim. Curabitur viverra,</p>
</section>
<div class="gallery abs">
  <span class="shot" role="img" aria-label="Snow-covered mountain cabins" style="left:16px;top:16px;width:232px;height:150px;background:linear-gradient(#6f8fc4,#e8edf4)"></span>
  <span class="shot" role="img" aria-label="Children in winter jackets lying in the snow" style="left:16px;top:180px;width:232px;height:150px;background:linear-gradient(#c9d3e6,#e7a7c6)"></span>
  <span class="shot" role="img" aria-label="Skiers on a sunny mountain slope" style="left:256px;top:16px;width:472px;height:314px;background:linear-gradient(#3f68b5 0%,#9fb8dc 45%,#e8ecf2 100%)"></span>
  <span class="shot" role="img" aria-label="Skier jumping through deep powder" style="left:736px;top:16px;width:230px;height:150px;background:linear-gradient(135deg,#1c3f8c,#dfe6f0)"></span>
  <span class="shot" role="img" aria-label="Snowy mountain valley" style="left:736px;top:180px;width:230px;height:150px;background:linear-gradient(#3d5f9a,#c7ced8)"></span>
</div>
<span class="btn-red find-btn abs">Find Out More</span>

<h2 class="section-title abs" style="top:1273px">Velmora Tours</h2>
<p class="section-lede abs" style="top:1330px">Lorem ipsum dolor sit amet, consectetur adipiscing elit. Etiam faucibus<br>diam a nibh ornare dignissim. Curabitur viverra,</p>

<!-- tour row 1 -->
<article class="tour-card abs" style="left:110px;top:1425px">
  <div class="tour-photo" role="img" aria-label="Mountains reflected in a calm lake" style="background:linear-gradient(#3c6eb4,#7a9a64 55%,#4d7fa8)"></div>
  <h3>NORWAY TOUR</h3><p class="tour-sub">Norway Winter Tours, start in Tromsø</p><hr>
  <p class="tour-desc">We offer a wide selection of Norway tours and holidays, both independent and escorted tours</p>
  <div class="price-band"><span>From € 699</span><span class="stars">★★★★★</span></div>
</article>
<article class="tour-card abs" style="left:359px;top:1425px">
  <div class="tour-photo" role="img" aria-label="Old town rooftops by the water" style="background:linear-gradient(#4f7fc2,#b87a55 60%,#6b5a4a)"></div>
  <h3>SWEDEN TOUR</h3><p class="tour-sub">Norway Winter Tours, start in Tromsø</p><hr>
  <p class="tour-desc">We offer a wide selection of Norway tours and holidays, both independent and escorted tours</p>
  <div class="price-band"><span>From € 699</span><span class="stars">★★★★★</span></div>
</article>
<article class="tour-card abs" style="left:608px;top:1425px">
  <div class="tour-photo" role="img" aria-label="Traveller in a red jacket resting on rocks" style="background:linear-gradient(#c8ccd2,#8f9298 55%,#b5312c 80%,#5c5f64)"></div>
  <h3>ICELAND TOUR</h3><p class="tour-sub">Norway Winter Tours, start in Tromsø</p><hr>
  <p class="tour-desc">We offer a wide selection of Norway tours and holidays, both independent and escorted tours</p>
  <div class="price-band"><span>From € 699</span><span class="stars">★★★★★</span></div>
</article>
<article class="tour-card abs" style="left:857px;top:1425px">
  <div class="tour-photo" role="img" aria-label="Green fjord with steep cliffs" style="background:linear-gradient(#5f8fcf,#3f7a3a 55%,#1f5c7a)"></div>
  <h3>FJORD TOUR</h3><p class="tour-sub">Norway Winter Tours, start in Tromsø</p><hr>
  <p class="tour-desc">We offer a wide selection of Norway tours and holidays, both independent and escorted tours</p>
  <div class="price-band"><span>From € 699</span><span class="stars">★★★★★</span></div>
</article>

<!-- tour row 2 -->
<article class="tour-card abs" style="left:110px;top:1839px">
  <div class="tour-photo" role="img" aria-label="Friends laughing in the snow" style="background:linear-gradient(#dfe3e8,#f2f2f2 50%,#b84a3a)"></div>
  <h3>WINTER,NORTHERN TOUR</h3><p class="tour-sub">Norway Winter Tours, start in Tromsø</p><hr>
  <p class="tour-desc">We offer a wide selection of Norway tours and holidays, both independent and escorted tours</p>
  <div class="price-band"><span>From € 699</span><span class="stars">★★★★★</span></div>
</article>
<article class="tour-card abs" style="left:359px;top:1839px">
  <div class="tour-photo" role="img" aria-label="City skyline with a tower at dusk" style="background:linear-gradient(#2b4d8f,#6a6f8a 50%,#c98a3f)"></div>
  <h3>CAPITALSTOUR</h3><p class="tour-sub">Norway Winter Tours, start in Tromsø</p><hr>
  <p class="tour-desc">We offer a wide selection of Norway tours and holidays, both independent and escorted tours</p>
  <div class="price-band"><span>From € 699</span><span class="stars">★★★★★</span></div>
</article>
<article class="tour-card abs" style="left:608px;top:1839px">
  <div class="tour-photo" role="img" aria-label="Collage of waterfall, meadows and travel scenes" style="background:linear-gradient(135deg,#3f6f8a,#5fae3c 50%,#2b5a8f)"></div>
  <h3>COMBINATION TOURS</h3><p class="tour-sub">Norway Winter Tours, start in Tromsø</p><hr>
  <p class="tour-desc">We offer a wide selection of Norway tours and holidays, both independent and escorted tours</p>
  <div class="price-band"><span>From € 699</span><span class="stars">★★★★★</span></div>
</article>
<article class="tour-card abs" style="left:857px;top:1839px">
  <div class="tour-photo" role="img" aria-label="Green aurora over a snowy lake" style="background:linear-gradient(#1a3a3a,#3fbf7a 45%,#1e3b4a 80%,#0f1f2a)"></div>
  <h3>NORTHERN LIGHTS</h3><p class="tour-sub">Norway Winter Tours, start in Tromsø</p><hr>
  <p class="tour-desc">We offer a wide selection of Norway tours and holidays, both independent and escorted tours</p>
  <div class="price-band"><span>From € 699</span><span class="stars">★★★★★</span></div>
</article>

<section class="testimonials abs">
  <h2 class="abs">WHAT OUR CUSTOMERS SAY</h2>
  <p class="summary abs">Curabitur accumsan consectetur gravida. In fells tincidunt, auctor massa amet, congue lorem. Morbi condimentum enim in aliquam vulputate. Integer ullamcorper porttitor dui, ornare sapien fermentum vitae.</p>
  <span class="chev abs" style="left:624px;top:124px">‹</span>
  <blockquote class="quote-box abs">Crabitur accumsan consectetur gravida. In fells tincidunt, amet, congue lorem. Morbi condimentum enim in aliquam ullamcorper porttitor dui, ornare sapien fermentum vitae.</blockquote>
  <span class="chev abs" style="left:1104px;top:124px">›</span>
  <div class="author abs"><span class="avatar" role="img" aria-label="Customer portrait"></span><span><b>Marten Holby</b>, Travelled to Kos Town 2014</span></div>
</section>

<section class="tweet-band abs">
  <span class="tweet-dot abs"></span>
  <p class="tweet-text abs">@&nbsp;&nbsp;<b><i>Travel</i></b>: 7 Incredible places you may have never heard of: http://vlm.to/4kQx2</p>
  <span class="tweet-nav abs" style="left:1012px">‹</span>
  <span class="tweet-nav abs" style="left:1044px">›</span>
</section>

<footer class="site-footer abs">
  <h4 style="left:114px">ABOUT VELMORA</h4>
  <p class="about-text abs">Lorem ipsum dolor sit amet, consectetur adipiscing elit. Etiam faucibus diam a nibh ornare dignissim. Curabitur viverra,turpis ac ultricies congue, purus risus tincidunt nisl, at rutrum nunc nulla a enim. Curabitur commodo dictum blandit. Fusce vulputate neque dolor, a pharetra justo elementum at. Praesent nec magna lectus.</p>
  <h4 style="left:490px">QUICK LINKS</h4>
  <ul class="quick-links abs">
    <li>Tour Types</li><li>Tour Selections</li><li>Winter Selections</li><li>Winter Tour Types</li><li>Recently Updated Tours</li><li>Velmora Journeys</li>
  </ul>
  <h4 style="left:720px">SIGN UP TO OUR NEWSLETTER</h4>
  <p class="news-text abs">Lorem ipsum dolor sit amet, consectetur adipiscing elit. Etiam faucibus</p>
  <div class="email abs">Enter Email</div>
  <span class="btn-red subscribe abs">SUBSCRIBE</span>
  <span class="foot-social abs" style="left:720px"></span>
  <span class="foot-social abs" style="left:748px"></span>
  <span class="foot-social abs" style="left:776px"></span>
  <span class="foot-social abs" style="left:804px"></span>
</footer>

<div class="bottom-bar abs">
  <span class="abs" style="left:114px;top:19px">© 2015 Velmora Journeys AS</span>
  <span class="pay-card abs" style="left:880px"></span>
  <span class="pay-card abs" style="left:936px"></span>
  <span class="pay-card abs" style="left:992px"></span>
  <span class="pay-card abs" style="left:1046px"></span>
</div>

</body>
</html>
```